Attorney business card for two offices

Looking for a new business card design that can list both of my offices, one in Houston and one in West Texas. Want something masculine, easy to read, and conservative yet somewhat modern. Our current card has used a nautical star on it for years, but I am not necessarily attached to that. Also, a lot of our forms use dark green and orange. Second office address is P.O. Box 518, Marathon, Texas 79615

```html
<!DOCTYPE html>
<html lang="en">
<head>
<meta charset="utf-8">
<title>Harlan Law Firm – Business Card</title>
<link rel="stylesheet" href="https://fonts.googleapis.com/css2?family=Cinzel:wght@400&family=Open+Sans:wght@400;600&display=swap">
<style>
  :root {
    --stage: #3a322c;
    --card-black: #050505;
    --card-white: #ffffff;
    --card-grey: #e4e5e6;
    --orange: #f05a28;
    --green: #2f8a3a;
    --ink: #2b2b2b;
  }
  * { box-sizing: border-box; margin: 0; padding: 0; }
  html, body { width: 1200px; height: 1200px; overflow: hidden; }
  body {
    background: var(--stage);
    font-family: "Open Sans", Arial, sans-serif;
    display: flex;
    flex-direction: column;
    align-items: center;
    justify-content: center;
    gap: 60px;
  }
  .card {
    width: 700px;
    height: 400px;
    position: relative;
    overflow: hidden;
    box-shadow: 0 10px 30px rgba(0,0,0,0.45);
  }
  /* Front */
  .card-front {
    background: var(--card-black);
    display: flex;
    flex-direction: column;
    align-items: center;
    justify-content: center;
    text-align: center;
  }
  .firm-name {
    color: var(--orange);
    font-weight: 600;
    font-size: 40px;
    letter-spacing: 2px;
    text-transform: uppercase;
  }
  .firm-tagline {
    margin-top: 6px;
    color: var(--green);
    font-family: "Cinzel", Georgia, serif;
    font-size: 15px;
    letter-spacing: 1.5px;
    text-transform: uppercase;
  }
  /* Back */
  .card-back {
    background: radial-gradient(ellipse at 50% 40%, var(--card-white) 0%, var(--card-white) 35%, var(--card-grey) 100%);
  }
  .back-content {
    position: absolute;
    top: 30px;
    left: 0;
    right: 0;
    text-align: center;
  }
  .attorney-name {
    color: var(--orange);
    font-size: 30px;
    font-weight: 400;
    letter-spacing: 1px;
    text-transform: uppercase;
  }
  .attorney-title {
    color: var(--ink);
    font-size: 17px;
    margin-top: 2px;
  }
  .star { display: block; margin: 12px auto; width: 20px; height: 20px; fill: var(--orange); }
  .contact-line { color: var(--orange); font-size: 18px; line-height: 1.55; }
  .address-line { color: var(--ink); font-size: 18px; line-height: 1.6; }
  .accent-band {
    position: absolute;
    left: 0; right: 0;
    bottom: 44px;
    height: 20px;
    background: var(--orange);
  }
  .band-base {
    position: absolute;
    left: 0; right: 0; bottom: 0;
    height: 44px;
    background: var(--card-white);
  }
</style>
</head>
<body>
  <section class="card card-front" aria-label="Card front">
    <h1 class="firm-name">The Harlan Law Firm, P.C</h1>
    <p class="firm-tagline">Power of Attorney &amp; Fee Agreement</p>
  </section>

  <section class="card card-back" aria-label="Card back">
    <div class="back-content">
      <h2 class="attorney-name">Dwight M. Harlan, Sr.</h2>
      <p class="attorney-title">Attorney of Law</p>
      <svg class="star" viewBox="0 0 24 24" aria-hidden="true"><polygon points="12,1 15,9 23,9 16.5,14 19,22 12,17 5,22 7.5,14 1,9 9,9"/></svg>
      <p class="contact-line">dwight@gulfplainslaw.com</p>
      <p class="contact-line">Tel. (713)555-0142 | Fax. (832)555-0187</p>
      <svg class="star" viewBox="0 0 24 24" aria-hidden="true"><polygon points="12,1 15,9 23,9 16.5,14 19,22 12,17 5,22 7.5,14 1,9 9,9"/></svg>
      <p class="address-line">P.O. Box 518, Marathon, Texas 79615</p>
      <p class="address-line">4410 Westheimer Road, suite 212, houston texax 77056</p>
    </div>
    <div class="accent-band"></div>
    <div class="band-base"></div>
  </section>
</body>
</html>
```